IT Company needs Website for new Web and Mobile products for Sports and Fitness

Background:

We developed web based white label frontend web solution, backend services and white label mobile apps for to log, analyze, share and control sport and fitness activities. The name of this product suite is "Trelvano" (http://trelvano-example.com)

This products will be used by customers that provide platforms and community systems for sport and fitness. One of the major USP's is, that our technology i open for nearly all common formats, devices and apps out in the market. This means, you can just upload your data directly from device, file or app - e.G. Brindle, Vextor, Kalppi, StrideNook, Jogmelda, BipBop and much others.

Two current concrete examples/References

(1) MyOrvane
It's an international platform from orvane for runners. It provides individual training lans and a training log. MyOrvane uses the Backend Product "Trelvano Hub" (see http://hub.trelvano-example.net for a landing page) to integrate device, file and app support. Before this, every user has to track his training with manual inputs

(2) Paceharbor and qel-zine
Both are German customers. Paceharor is focused on runners. qel-zine is focused on Triatheletes. Both use the Product "Trelvano Web". This is a complete web solution with web based frontend solutions for athletes and coaches.

What do we need?
We need website layout for B2B for our products. We don't need lot's of pages. We need the pretty and nice layout, so we can derive the pages we need.

IMPORTANT
We don't talk about the webpages for the product itself (this will be a different project in future). We talk about a website, explaining the products)
Updates

Hi all,

we just start reviewing the first designs, and try to give feedback as detailed as possible. We attached a PDF document, to describe the the products a little bit more detailed. 

As written in the description, in the end we have two different sections. One is the usual stuff like "start page", "about", "contact", "disclaimer", "pricing", "blah...." and one will be the Developer Section, the "Tec Section". This ist aimed to developers (of our customers) that will integrate our products in there existing system or which will integrate our services in there own software.  This "pages" are more like "documentation", so easy to read and cool to look at (cause developers likes it cool, but straight)

Dear all,

we just do the final review. Cause this week is with heavy load, it takes some time...

Cheers

Ulrik

Target Market(s)

* Platforms and Communities for sport, health and fitness
* Gyms

Industry/Entity Type

Concrete

Font styles to use
Sans Serif

Requirements
Must have
• * Templates shall base on bootstrap. If not, it shall be easily realized on our site with bootstrap or out of the box "full responsive"

* HTML5 / CSS3
Nice to have
• PAGES
- Start Page
- Generic Template (from which we can derive additional pages)
- Contact Page
- Disclaimer Page
- Blog/News Page
- "About us" Page (can be combined with disclaimer)
- One Example product page (in end we have 3 products), shall show (if you need product details, let me know)
- product and it's description
- pricing information
- Add-Ons for the product
- Developer Section Page (Start Point for developers, where the finde "basic technical concepts and developer API's
- Example Developer Page for technical concept
- Example Developer Page for API

LOGO ISSUE
You can use an align to the Logo attached OR provide a new logo. The given logo is a logo for our own B2C Website http://trelvano-example.net. It's not really necessary, that the logo or the color must be used for the product website. Maybe it will be better if it's a complete new one, to avoid irritation between Trelvano as a B2B product and trelvano-example.net as a B2C platform.
Should not have
• No Flash and other proprietary technologies

```html
<!DOCTYPE html>
<html lang="en">
<head>
<meta charset="utf-8">
<title>Trelvano — Get Smarter Stuff</title>
<link rel="stylesheet" href="https://fonts.googleapis.com/css2?family=Open+Sans:wght@400;600;700&display=swap">
<style>
  :root {
    --brand-blue: #1a72e0;
    --text-dark: #333333;
    --text-body: #3a3a3a;
    --nav-text: #2f2f2f;
    --header-bg: #ffffff;
    --hero-bg-light: #f1f1f1;
    --hero-bg-dark: #dcdcdc;
    --divider: #cfcfcf;
    --menu-border: #ececec;
    --button-grey: #555555;
  }
  * { margin: 0; padding: 0; box-sizing: border-box; }
  html, body { width: 1200px; height: 478px; overflow: hidden; }
  body {
    position: relative;
    font-family: "Open Sans", Arial, sans-serif;
    background: linear-gradient(100deg, var(--hero-bg-light) 0%, #e6e6e6 55%, var(--hero-bg-dark) 100%);
  }
  a { text-decoration: none; }
  .site-header {
    position: absolute; left: 0; top: 0; width: 1200px; height: 70px;
    background: var(--header-bg);
    box-shadow: 0 2px 6px rgba(0,0,0,0.12);
    z-index: 3;
  }
  .brand {
    position: absolute; left: 62px; top: 14px;
    display: flex; align-items: center; gap: 8px;
    font-size: 26px; font-weight: 700; color: var(--brand-blue);
  }
  .brand-mark { width: 16px; height: 16px; background: var(--brand-blue); }
  .main-nav {
    position: absolute; top: 24px; left: 619px;
    display: flex; gap: 28px;
    font-size: 13px; font-weight: 600; text-transform: uppercase;
  }
  .main-nav a { color: var(--nav-text); }
  .main-nav a.is-current { color: var(--brand-blue); }
  .dropdown-menu {
    position: absolute; left: 742px; top: 62px; width: 169px;
    background: #fff; box-shadow: 0 2px 6px rgba(0,0,0,0.15);
    list-style: none; z-index: 4;
  }
  .dropdown-menu li {
    height: 36.7px; line-height: 36.7px; padding-left: 15px;
    font-size: 11px; text-transform: uppercase; color: var(--text-dark);
    border-bottom: 1px solid var(--menu-border);
  }
  .dropdown-menu li:last-child { border-bottom: none; }
  .dropdown-menu li.is-active { background: var(--brand-blue); color: #fff; }
  .hero-photo {
    position: absolute; left: 565px; top: 120px; width: 530px; height: 358px;
    background: linear-gradient(180deg, #d9d9d9 0%, #c9ccd0 60%, #b8bcc2 100%);
    border-radius: 14px 14px 0 0; z-index: 1;
  }
  .hero-copy { position: absolute; left: 71px; top: 146px; width: 513px; z-index: 2; }
  .hero-kicker { font-size: 21px; color: var(--text-dark); line-height: 28px; white-space: nowrap; }
  .hero-title {
    margin-top: 7px; font-size: 50px; font-weight: 700; color: var(--brand-blue);
    line-height: 60px; white-space: nowrap;
  }
  .divider { height: 1px; background: var(--divider); }
  .hero-title + .divider { margin-top: 17px; }
  .hero-text { margin: 20px 0; font-size: 14px; line-height: 24px; color: var(--text-body); width: 513px; }
  .hero-actions { position: absolute; left: 71px; top: 401px; display: flex; gap: 19px; z-index: 2; }
  .btn {
    height: 43px; display: flex; align-items: center; justify-content: center; gap: 9px;
    border: 1px solid; border-radius: 2px; font-size: 16px; text-transform: uppercase;
    background: transparent;
  }
  .btn-primary { width: 172px; color: var(--brand-blue); border-color: var(--brand-blue); }
  .btn-secondary { width: 155px; color: var(--button-grey); border-color: var(--button-grey); }
  .btn svg { width: 15px; height: 15px; }
</style>
</head>
<body>
  <header class="site-header">
    <div class="brand"><span class="brand-mark"></span>Trelvano</div>
    <nav class="main-nav">
      <a href="#" class="is-current">Home</a>
      <a href="#">Pages</a>
      <a href="#">Features</a>
      <a href="#">Portfolio</a>
      <a href="#">Blog</a>
      <a href="#">Contact</a>
    </nav>
  </header>

  <ul class="dropdown-menu">
    <li>Elements</li>
    <li>Typography</li>
    <li class="is-active">Pricing Tables</li>
    <li>Page Columns</li>
    <li>Testimonials</li>
    <li>FAQs</li>
    <li>Tabs</li>
    <li>Custom Colors</li>
    <li>Clean &amp; Valid Code</li>
    <li>Useful Typo Elements</li>
    <li>Cross Browser Check</li>
  </ul>

  <div class="hero-photo" role="img" aria-label="Hands holding a white tablet showing web design graphics"></div>

  <section class="hero-copy">
    <p class="hero-kicker">Find the Benefits of Using Our Products.</p>
    <h1 class="hero-title">GET SMARTER STUFF!</h1>
    <div class="divider"></div>
    <p class="hero-text">Many desktop publishing packages and web page editors now use the lorem Ipsum as their default model text, and a search for 'lorem ipsum will uncover many web sites still in their infancy.</p>
    <div class="divider"></div>
  </section>

  <div class="hero-actions">
    <a class="btn btn-primary" href="#">
      <svg viewBox="0 0 16 16" aria-hidden="true"><path d="M15 1 1 7.5l6 1.5 1.5 6z" fill="currentColor"/></svg>
      Get Started
    </a>
    <a class="btn btn-secondary" href="#">
      <svg viewBox="0 0 16 16" aria-hidden="true" fill="none" stroke="currentColor" stroke-width="1.3"><rect x="1" y="7" width="3" height="7"/><path d="M4 7.5 7 2c1.2 0 1.8.8 1.5 2L8 6.5h5c.9 0 1.5.8 1.3 1.6l-1.2 5c-.2.6-.7.9-1.3.9H4"/></svg>
      Buy Now!
    </a>
  </div>
</body>
</html>
```